"Career in Gradimar" | Poster design

We need a "We are hiring" poster design. We are a construction company based in Croatia and we are looking for 3 categories of construction workers. We want moder, serious and powerful poster . In attachment you can find our logo. The font of a text that is used in logo design is "nexa bold".

At the bottom (or where designer can see it) will be description of general condition. The poster must be simple and clear.

Target Market(s)

Wide range of employment

Industry/Entity Type

Construction Company

Colors

Designer to choose colors to be used in the design.

Requirements
Must have
• The text in poster that will be needed is "Mason/carpenter job", "Steel-bender job" and "Auxiliary worker". This terms may be wrong, but it will be translated in local language. Under all of them will be a short descrtiption row, and one row of salary. This is for all three categories.
• At the bottom (or where designer can see it) will be description of general condition. The poster must be simple and clear.

```html
<!DOCTYPE html>
<html lang="en">
<head>
<meta charset="utf-8">
<title>Career in Gradimar – We Are Hiring</title>
<link href="https://fonts.googleapis.com/css2?family=Bebas+Neue&family=Montserrat:wght@600&family=Oswald:wght@500&family=Roboto+Condensed:wght@400;700&display=swap" rel="stylesheet">
<style>
  :root {
    --frame: #8a8a8a;
    --paper: #f4f4f4;
    --stripe: #e6e6e6;
    --ink: #2b2b2b;
    --orange: #ee7d22;
    --rust: #c8651e;
    --rule: #c4c4c4;
    --muted: #444444;
    --crowd-warm: #efd7bd;
    --crowd-mid: #e3d2c3;
    --crowd-cool: #d2d8d3;
  }
  * { margin: 0; padding: 0; box-sizing: border-box; }
  html, body {
    width: 846px; height: 1200px; overflow: hidden;
    background: var(--frame);
  }
  .poster {
    position: absolute; left: 32px; top: 47px;
    width: 776px; height: 1096px;
    background:
      repeating-linear-gradient(135deg, transparent 0 7px, var(--stripe) 7px 9px),
      var(--paper);
    overflow: hidden;
  }
  .poster::before {
    content: ""; position: absolute; inset: 0;
    background: radial-gradient(ellipse at 50% 45%, rgba(255,255,255,0.95) 0%, rgba(255,255,255,0.7) 45%, rgba(255,255,255,0) 80%);
  }
  .poster > * { position: absolute; }

  .brand { left: 526px; top: 50px; width: 210px; text-align: center; }
  .brand-square {
    display: block; width: 70px; height: 70px; margin: 0 auto 10px;
    border: 2px solid #555;
  }
  .brand-name {
    font-family: "Montserrat", sans-serif; font-weight: 600;
    font-size: 25px; line-height: 28px; letter-spacing: 2px; color: var(--orange);
  }
  .brand-tagline {
    font-family: "Roboto Condensed", sans-serif; font-weight: 700;
    font-size: 9px; color: var(--muted); letter-spacing: 0.3px; margin-top: 1px;
    white-space: nowrap;
  }

  .headline {
    left: 47px; top: 160px;
    font-family: "Bebas Neue", sans-serif; font-size: 77px; line-height: 70px;
    color: var(--ink); letter-spacing: 1px; font-weight: 400;
  }
  .headline .accent { color: var(--orange); }

  .crowd-arrow {
    left: 133px; top: 358px; width: 476px; height: 456px;
    border-radius: 4px;
    background: linear-gradient(160deg, var(--crowd-warm) 0%, var(--crowd-mid) 50%, var(--crowd-cool) 100%);
  }

  .jobs {
    left: 33px; top: 843px; width: 710px; height: 84px;
    border-top: 1px solid var(--rule); border-bottom: 1px solid var(--rule);
    display: flex;
  }
  .job {
    flex: 1; text-align: center; padding-top: 13px;
    font-family: Arial, sans-serif; font-weight: 700; font-size: 11px; line-height: 13px; color: var(--ink);
  }
  .job + .job { border-left: 1px solid var(--rule); margin: 12px 0 10px; padding-top: 1px; }
  .job-title {
    font-family: "Oswald", sans-serif; font-weight: 500; font-size: 18px; line-height: 22px;
    color: var(--orange); text-transform: uppercase;
  }

  .contact {
    left: 0; width: 776px; top: 982px; text-align: center;
    font-family: "Roboto Condensed", sans-serif; font-weight: 700; font-size: 20px; color: var(--rust);
  }
  .contact .sep { margin: 0 8px; }

  .terms {
    left: 50px; top: 1017px; width: 676px;
    font-family: "Roboto Condensed", sans-serif; font-size: 8px; line-height: 9.5px; color: var(--ink);
  }
</style>
</head>
<body>
  <main class="poster">
    <div class="brand">
      <span class="brand-square"></span>
      <div class="brand-name">GRADIMAR</div>
      <div class="brand-tagline">IZVOĐENJE I VOĐENJE GRAĐEVINSKIH RADOVA</div>
    </div>

    <h1 class="headline">FINDING THE<br><span class="accent">RIGHT</span> CANDIDATE</h1>

    <div class="crowd-arrow" role="img" aria-label="Illustration of many small people in colourful clothes standing together in a formation, with a few people walking around them"></div>

    <section class="jobs">
      <div class="job">
        <div class="job-title">Mason/Carpenter Job</div>
        of them of them Under all of theof them<br>m will be a short descrtiption row<br>Sallery $85000
      </div>
      <div class="job">
        <div class="job-title">Steel-Bender Job</div>
        of them of them Under all of theof them<br>m will be a short descrtiption row<br>Sallery $85000
      </div>
      <div class="job">
        <div class="job-title">Auxiliary Worker</div>
        of them of them Under all of theof them<br>m will be a short descrtiption row<br>Sallery $85000
      </div>
    </section>

    <p class="contact">ph. 10987654321<span class="sep">|</span>email: jobs@gradimar-posao.com</p>

    <p class="terms">Terms &amp; Conditions: applications are accepted until all positions are filled. Candidates must hold valid work documents and be able to start within thirty days. Accommodation and transport to site are provided for workers outside the city. Salary is stated in gross annual amount and depends on experience. Only shortlisted candidates will be contacted for an interview. Previous construction experience is an advantage but not required for auxiliary roles. Gradimar is an equal opportunity employer and welcomes applicants from all backgrounds and regions.</p>
  </main>
</body>
</html>
```